Harbourline Plumbing business card full re design & logo design

Harbourline Plumbing is a Sydney based mechanical plumbing contractor company.
We would like a full redesign with new logo etc which we can take to a future website, uniforms, vehicle sign writing etc.
Blue is my preferred choice of colour but i would be open to see a couple of alternatives thrown in the mix to see how they compare. I am open to see on white cards, black cards etc. Open to many new ideas.
Please see attached original business cards which have been used for the last 5 years.

Target Market(s)

Mechanical services industry.

Industry/Entity Type

Plumbing

Contact Information for Business Card

Colin Ashdale
Director

Mob: 0427 590 614
Email: colin@harbourlineplumbing.net.au
PO BOX 816
Merrowdale NSW 2159
Lic: 583106k

Logo Text

Harbourline Plumbing

Font styles to use
Sans Serif

Colors
0655a3
3276b5
0792cd
33a6d7
85cae6
000000
333333
474747

Requirements
Must have
• Things that make it very professional and very well presented.
Nice to have
• Same description or very similar to attached uploaded file
Should not have
• Anything that makes it look unprofessional or cartoony.

```html
<!DOCTYPE html>
<html lang="en">
<head>
<meta charset="utf-8">
<title>Harbourline Plumbing – Business Cards</title>
<link rel="stylesheet" href="https://fonts.googleapis.com/css2?family=Montserrat:wght@400;500;700&display=swap">
<style>
  :root {
    --brand-blue: #0655a3;
    --mid-blue: #3276b5;
    --ink: #333333;
    --ink-soft: #474747;
    --card-white: #ebebef;
    --card-black: #000000;
    --backdrop: #d9d6d1;
  }
  * { box-sizing: border-box; margin: 0; padding: 0; }
  html, body {
    width: 1200px;
    height: 800px;
    overflow: hidden;
  }
  body {
    background: var(--backdrop);
    font-family: "Montserrat", sans-serif;
    display: flex;
    align-items: center;
    justify-content: center;
    gap: 50px;
  }
  .card {
    width: 525px;
    height: 300px;
    position: relative;
    box-shadow: 0 10px 28px rgba(0,0,0,0.18);
  }
  .card--front { background: var(--card-white); }
  .card--back {
    background: var(--card-black);
    display: flex;
    align-items: center;
    justify-content: center;
  }

  .wordmark {
    display: flex;
    flex-direction: column;
    align-items: center;
    gap: 10px;
    color: var(--brand-blue);
    font-weight: 700;
    text-transform: uppercase;
    text-align: center;
    line-height: 1.1;
  }
  .wordmark__square {
    width: 38px;
    height: 38px;
    background: var(--brand-blue);
  }
  .wordmark__name { display: block; }
  .wordmark__line--main { font-size: 25px; letter-spacing: 0.5px; }
  .wordmark__line--sub { font-size: 12px; letter-spacing: 6px; }

  .card--front .wordmark {
    position: absolute;
    left: 30px;
    top: 92px;
    width: 230px;
  }
  .card--back .wordmark__square { width: 56px; height: 56px; }
  .card--back .wordmark__line--main { font-size: 36px; }
  .card--back .wordmark__line--sub { font-size: 16px; letter-spacing: 9px; }

  .contact {
    position: absolute;
    left: 285px;
    top: 48px;
    color: var(--ink);
    font-size: 11.5px;
    line-height: 1.45;
  }
  .contact__name {
    color: var(--brand-blue);
    font-weight: 700;
    font-size: 18px;
    line-height: 1.1;
  }
  .contact__role { margin-bottom: 18px; color: var(--ink-soft); }
  .contact__address { margin-bottom: 18px; font-style: normal; }
</style>
</head>
<body>
  <article class="card card--front">
    <div class="wordmark">
      <span class="wordmark__square"></span>
      <span class="wordmark__name">
        <span class="wordmark__line--main">Harbourline</span><br>
        <span class="wordmark__line--sub">Plumbing</span>
      </span>
    </div>
    <div class="contact">
      <p class="contact__name">Colin Ashdale</p>
      <p class="contact__role">Director</p>
      <address class="contact__address">
        PO BOX 816<br>
        Merrowdale NSW 2159<br>
        Lic: 583106k
      </address>
      <p class="contact__phone">0427 590 614</p>
      <p class="contact__email">colin@harbourlineplumbing.net.au</p>
    </div>
  </article>

  <article class="card card--back">
    <div class="wordmark">
      <span class="wordmark__square"></span>
      <span class="wordmark__name">
        <span class="wordmark__line--main">Harbourline</span><br>
        <span class="wordmark__line--sub">Plumbing</span>
      </span>
    </div>
  </article>
</body>
</html>
```